Business Card Design

New business card design

Target Market(s)

Residential & Commercial Property Managers

Industry/Entity Type

Plumbing Services

Contact Information for Business Card

Name - Tom Brereton, title - Director, Phone Number - 0431 862 517, email - tom@rvk-plumbing.com.au, Company ABN - 73 512 938 204,

Font styles to use
Sans Serif

Colors
0054AA
0677BA
7BADD7
CADEEF
E8F1F8

```html
<!DOCTYPE html>
<html lang="en">
<head>
<meta charset="utf-8">
<title>Kinsley Plumbing – Business Card</title>
<link href="https://fonts.googleapis.com/css2?family=Poppins:wght@400;600&family=Roboto:wght@300;400&display=swap" rel="stylesheet">
<style>
  :root {
    --stage: #2b2b2d;
    --card-white: #f4f4f2;
    --card-black: #1c1c1e;
    --edge-taupe: #6f6661;
    --ink: #1e1e1e;
    --ink-soft: #8a8a8a;
    --accent: #0677BA;
    --logo-white: #ffffff;
  }
  * { box-sizing: border-box; margin: 0; padding: 0; }
  html, body {
    width: 1200px; height: 852px; overflow: hidden;
    background: var(--stage);
  }
  .stage { position: relative; width: 1200px; height: 852px; }

  .card {
    position: absolute; top: 276px;
    width: 520px; height: 300px;
    border-radius: 22px; overflow: hidden;
  }
  .card-back { left: 50px; background: var(--card-black); }
  .card-front { left: 630px; background: var(--card-white); }

  .drop-pattern {
    position: absolute; inset: 0;
    background: linear-gradient(160deg, #3a3a3c 0%, #1f1f21 45%, #0b0b0c 100%);
  }

  .front-shapes { position: absolute; inset: 0; }

  .holder {
    position: absolute; left: 36px; top: 132px;
    font-family: "Poppins", sans-serif;
  }
  .holder-name { font-size: 19px; font-weight: 600; color: var(--ink); line-height: 1.1; }
  .holder-title { font-family: "Roboto", sans-serif; font-size: 12px; font-weight: 300; color: var(--ink-soft); margin-top: 2px; }

  .contact {
    position: absolute; left: 36px; top: 186px;
    font-family: "Roboto", sans-serif; font-size: 11.5px; color: var(--ink);
    line-height: 16px;
  }
  .contact-address { margin-bottom: 2px; }
  .contact-row { display: flex; align-items: center; gap: 8px; }
  .contact-row svg { width: 11px; height: 11px; flex: none; }

  .brand {
    position: absolute; left: 292px; top: 112px; width: 210px;
    display: flex; align-items: center; justify-content: center; gap: 8px;
    font-family: "Poppins", sans-serif; font-weight: 400; font-size: 21px;
    color: var(--logo-white); white-space: nowrap;
  }
  .brand-dot { width: 10px; height: 10px; border-radius: 50%; background: var(--accent); flex: none; }
</style>
</head>
<body>
<div class="stage">

  <section class="card card-back">
    <div class="drop-pattern" role="img" aria-label="Repeating pattern of glossy dark water drops with one blue drop accent"></div>
  </section>

  <section class="card card-front">
    <svg class="front-shapes" viewBox="0 0 520 300" aria-hidden="true">
      <circle cx="464" cy="118" r="230" fill="var(--edge-taupe)"/>
      <circle cx="470" cy="110" r="230" fill="var(--card-black)"/>
    </svg>

    <div class="brand">
      <span class="brand-name">Kinsley Plumbing</span>
      <span class="brand-dot"></span>
    </div>

    <div class="holder">
      <p class="holder-name">Dale Kinsley</p>
      <p class="holder-title">Managing Director</p>
    </div>

    <div class="contact">
      <p class="contact-address">17 Harbour Rd., Port Ellis,<br>Westbrook, US 402187</p>
      <p class="contact-row">
        <svg viewBox="0 0 12 12"><path fill="var(--accent)" d="M2.5 1h2l1 3-1.4 1a6.5 6.5 0 0 0 2.9 2.9l1-1.4 3 1v2a1.5 1.5 0 0 1-1.5 1.5A9.5 9.5 0 0 1 1 2.5 1.5 1.5 0 0 1 2.5 1z"/></svg>
        555-014-2278
      </p>
      <p class="contact-row">
        <svg viewBox="0 0 12 12"><rect x="0.5" y="2" width="11" height="8" rx="1" fill="var(--accent)"/><path d="M1 2.8 6 6.6 11 2.8" fill="none" stroke="#fff" stroke-width="1"/></svg>
        dale@kinsleyplumbing.com
      </p>
      <p class="contact-row">
        <svg viewBox="0 0 12 12"><circle cx="6" cy="6" r="5.5" fill="var(--accent)"/><path d="M0.5 6h11M6 0.5c-2.5 3-2.5 8 0 11M6 0.5c2.5 3 2.5 8 0 11" fill="none" stroke="#fff" stroke-width="0.8"/></svg>
        www.kinsleyplumbing.com
      </p>
    </div>
  </section>

</div>
</body>
</html>
```